Carpet cleaning company wants business card

Need an exciting new fresh design for business cards for my carpet cleaning /pest control business
www.tidewellhomecare.com.au
Can design include a lined section for quoting or information? Thanks !

```html
<!DOCTYPE html>
<html lang="en">
<head>
<meta charset="utf-8">
<title>Tidewell Home Care – Business Card</title>
<link rel="stylesheet" href="https://fonts.googleapis.com/css2?family=Poppins:wght@400;500;700;800&display=swap">
<style>
  :root {
    --stage: #222223;
    --card-dark: #1f1f22;
    --card-red: #ec3b38;
    --brand-red: #e93a36;
    --brand-blue: #1d5fb0;
    --ink-light: #f2f2f2;
    --ink-soft: #d9d9dc;
  }
  * { box-sizing: border-box; margin: 0; padding: 0; }
  html, body {
    width: 1200px; height: 780px; overflow: hidden;
    background: var(--stage);
    font-family: "Poppins", sans-serif;
  }
  .stage {
    position: relative; width: 1200px; height: 780px;
    display: flex; align-items: center; justify-content: center; gap: 40px;
  }
  .card {
    width: 540px; height: 310px; position: relative;
    box-shadow: 0 18px 40px rgba(0,0,0,.55);
    overflow: hidden;
  }
  /* Contact face */
  .card--contact {
    background: var(--card-dark);
    color: var(--ink-light);
    padding: 24px 40px;
    display: flex; flex-direction: column; align-items: center; justify-content: center; text-align: center;
  }
  .card--contact::before {
    content: ""; position: absolute; left: 0; right: 0; top: 62px; height: 60px;
    background: linear-gradient(180deg, rgba(0,0,0,0) 0%, rgba(0,0,0,.28) 50%, rgba(0,0,0,0) 100%);
  }
  .brand-name {
    position: relative;
    display: flex; align-items: center; gap: 10px;
    font-weight: 800; font-size: 30px; line-height: 1.2; letter-spacing: -.5px;
    color: var(--brand-red);
  }
  .brand-mark { width: 14px; height: 14px; background: var(--brand-blue); flex: none; }
  .person { position: relative; margin-top: 14px; }
  .person__name { font-size: 30px; line-height: 1.1; }
  .person__first { color: var(--brand-red); font-weight: 700; }
  .person__last { color: var(--brand-blue); font-weight: 400; }
  .person__role { font-size: 13px; line-height: 1.4; font-weight: 500; color: var(--ink-light); margin-top: 2px; }
  .contact-icons { position: relative; display: flex; gap: 6px; margin-top: 10px; }
  .icon-dot {
    width: 20px; height: 20px; border-radius: 50%; background: var(--brand-red);
    display: flex; align-items: center; justify-content: center; flex: none;
  }
  .icon-dot svg { width: 11px; height: 11px; fill: #fff; }
  .contact-list { position: relative; list-style: none; margin-top: 6px; font-size: 12.5px; color: var(--ink-soft); line-height: 1.55; }
  .address { position: relative; margin-top: 10px; display: flex; flex-direction: column; align-items: center; gap: 4px; font-size: 12.5px; line-height: 1.4; color: var(--ink-soft); }

  /* Brand face */
  .card--brand {
    background: var(--card-red);
    display: flex; align-items: center; justify-content: center;
  }
  .card--brand .brand-name { color: #ffffff; font-size: 42px; gap: 14px; }
  .card--brand .brand-mark { width: 18px; height: 18px; background: #ffffff; }
</style>
</head>
<body>
<main class="stage">
  <section class="card card--contact" aria-label="Business card, contact side">
    <div class="brand-name"><span class="brand-mark"></span>Tidewell Home Care</div>
    <div class="person">
      <p class="person__name"><span class="person__first">Maren</span> <span class="person__last">Doyle</span></p>
      <p class="person__role">Founder &amp; CEO</p>
    </div>
    <div class="contact-icons">
      <span class="icon-dot"><svg viewBox="0 0 24 24"><path d="M6.6 10.8a15.1 15.1 0 0 0 6.6 6.6l2.2-2.2c.3-.3.7-.4 1-.2 1.1.4 2.3.6 3.6.6.6 0 1 .4 1 1V20c0 .6-.4 1-1 1A17 17 0 0 1 3 4c0-.6.4-1 1-1h3.5c.6 0 1 .4 1 1 0 1.3.2 2.5.6 3.6.1.3 0 .7-.2 1z"/></svg></span>
      <span class="icon-dot"><svg viewBox="0 0 24 24"><path d="M12 2a10 10 0 1 0 0 20 10 10 0 0 0 0-20zm0 2c1 0 2.3 1.8 2.9 5H9.1C9.7 5.8 11 4 12 4zM4.3 11h3.6a20 20 0 0 0 0 2H4.3a8 8 0 0 1 0-2zm4.8 4h5.8c-.6 3.2-1.9 5-2.9 5s-2.3-1.8-2.9-5zm7-2a20 20 0 0 0 0-2h3.6a8 8 0 0 1 0 2z"/></svg></span>
      <span class="icon-dot"><svg viewBox="0 0 24 24"><path d="M3 5h18v14H3zm2 2v.5l7 4.5 7-4.5V7z"/></svg></span>
    </div>
    <ul class="contact-list">
      <li>07 5120 4488</li>
      <li>www.tidewellhomecare.com.au</li>
      <li>admin@tidewellhomecare.com.au</li>
    </ul>
    <div class="address">
      <span class="icon-dot"><svg viewBox="0 0 24 24"><path d="M12 2a7 7 0 0 0-7 7c0 5 7 13 7 13s7-8 7-13a7 7 0 0 0-7-7zm0 9.5a2.5 2.5 0 1 1 0-5 2.5 2.5 0 0 1 0 5z"/></svg></span>
      <p>48 Harbourview Lane, Noosa, QLD 4567</p>
    </div>
  </section>

  <section class="card card--brand" aria-label="Business card, brand side">
    <div class="brand-name"><span class="brand-mark"></span>Tidewell Home Care</div>
  </section>
</main>
</body>
</html>
```